We need a brochure for our project Caelum Petra

Hi!
We need a brochure for our project!
The designer can check out our website: caelum-petrix.com (to see what it's about)
The designer can choose the brochure layout and fold, as the designer sees fit. The designer can also format text as he sees fit.
We'd like the style to be minimal, but still not too blank, (if it makes sense).
Our name is Caelum Petra, meaning Sky Stone, so think in terms of green and brown, environmental.
We are attaching materials that should go on the brochure, as well as text, also the explanation of the render since some arrows should be added to point to what is going in and what goes out. What we want to present is a circular economy around the render.
I will also attach the work our previous designer did, and we would go for something different at this point (but the image inside shows circular economy and what goes out and in well, so that should somehow be transferred around the render).

Thank you,
Caelum Petra team

```html
<!DOCTYPE html>
<html lang="en">
<head>
<meta charset="utf-8">
<title>Caelum Petra – Brochure</title>
<link rel="stylesheet" href="https://fonts.googleapis.com/css2?family=Roboto:ital,wght@0,400;0,500;0,700;1,400;1,500;1,700&family=Roboto+Condensed:ital,wght@0,700;1,700;1,900&family=Montserrat:wght@600;700&display=swap">
<style>
:root{
  --backdrop:#6aa83b;
  --leaf:#7cc242;
  --leaf-light:#a6d65a;
  --leaf-dark:#3f8f1f;
  --forest:#2e5416;
  --sky:#1a7fe0;
  --sky-bright:#2aaaf2;
  --ink:#222;
  --ink-soft:#444;
  --soil:#6b3f2a;
  --white:#fff;
}
*{margin:0;padding:0;box-sizing:border-box}
html,body{width:801px;height:1200px;overflow:hidden}
body{background:var(--backdrop);font-family:"Roboto",sans-serif;color:var(--ink);position:relative}
.sheet{position:absolute;width:697px;background:var(--white);overflow:hidden}
.sheet--outside{left:52px;top:45px;height:539px}
.sheet--inside{left:53px;top:617px;height:537px}
.sheet > *{position:absolute}
.shapes{left:0;top:0;width:100%;height:100%}

/* shared */
.pill{display:flex;align-items:center;gap:5px;background:var(--sky);color:var(--white);white-space:nowrap;
  font-family:"Roboto Condensed",sans-serif;font-style:italic;font-weight:900;border-radius:0 12px 12px 0;padding:0 8px 0 6px;letter-spacing:.3px}
.pill::before{content:"";width:12px;height:12px;border:2.5px solid var(--white);border-radius:50%;flex:none}
.bullets{list-style:none;font-size:8.5px;line-height:12px;color:var(--ink)}
.bullets li{position:relative;padding-left:9px}
.bullets li::before{content:"";position:absolute;left:0;top:4px;width:4px;height:4px;border-radius:50%;background:var(--sky)}
.bullets b{font-style:italic;font-weight:700}
.url{font-family:"Montserrat",sans-serif;font-weight:600;font-size:10px;letter-spacing:1.2px;color:var(--white);text-align:center;width:233px}

/* outside */
.brand{left:500px;top:18px;display:flex;align-items:center;gap:6px;white-space:nowrap;font-family:"Roboto",sans-serif;font-weight:500;font-size:15px;letter-spacing:1.3px;color:var(--forest)}
.brand__dot{width:22px;height:22px;border-radius:50%;background:var(--leaf-dark)}
.challenge__title{left:4px;top:291px;height:23px;font-size:17px;width:188px}
.challenge__lead{left:0;width:208px;top:323px;text-align:right;font-style:italic;font-size:11px;color:var(--ink)}
.challenge__list{left:19px;top:343px;width:192px}
.challenge__list li{margin-bottom:12px}
.certified{left:0;width:233px;top:463px;text-align:center;font-family:"Roboto Condensed",sans-serif;font-style:italic;font-weight:700;font-size:6.5px;line-height:8px;color:var(--ink);text-transform:uppercase}
.certified .hl{color:var(--sky-bright);font-size:10px;line-height:11px}
.certified .hl--big{font-size:12px;line-height:13px}
.certified::after{content:"";display:block;width:120px;height:1px;background:#999;margin:4px auto 0}
.connect__title{left:253px;top:343px;font-family:"Montserrat",sans-serif;font-weight:700;font-size:14px;color:var(--forest)}
.connect__box{left:243px;top:363px;width:214px;height:145px;border-radius:9px;background:rgba(255,255,255,.28)}
.contact{left:258px;display:flex;gap:11px;align-items:flex-start;font-size:7.8px;line-height:10.5px;color:var(--ink)}
.contact__icon{width:22px;height:22px;border-radius:50%;background:var(--sky-bright);box-shadow:0 0 0 3px rgba(255,255,255,.6);display:flex;align-items:center;justify-content:center;flex:none;margin-top:4px}
.contact__label{font-family:"Montserrat",sans-serif;font-weight:700;font-size:8px;color:var(--forest);margin-bottom:2px}
.contact--address{top:369px}
.contact--phone{top:417px}
.contact--email{top:466px}
.mission{left:470px;width:210px;top:361px;text-align:center}
.mission__kicker{font-family:"Roboto Condensed",sans-serif;font-weight:700;font-size:12px;color:var(--forest);letter-spacing:.2px;white-space:nowrap}
.mission__head{font-family:"Roboto Condensed",sans-serif;font-weight:700;font-size:25px;line-height:28px;color:var(--white);white-space:nowrap}
.mission__line{font-family:"Roboto Condensed",sans-serif;font-style:italic;font-weight:700;font-size:8.5px;line-height:11.5px;color:var(--forest);margin-top:6px}
.mission__line span{color:var(--white)}
.mission__tag{display:inline-block;margin-top:4px;background:linear-gradient(#fff,#dcdcdc);border-radius:8px;padding:1px 22px;font-family:"Roboto Condensed",sans-serif;font-style:italic;font-weight:900;font-size:11px;color:var(--forest)}
.direct{right:28px;top:495px;text-align:right;color:var(--white)}
.direct__phone{font-family:"Roboto Condensed",sans-serif;font-weight:700;font-size:14px}
.direct__web{font-family:"Montserrat",sans-serif;font-weight:600;font-size:10.5px;margin-top:3px}

/* inside */
.spec{left:367px;top:56px;font-family:"Roboto Condensed",sans-serif;font-style:italic;font-weight:700;font-size:7px;line-height:10px;color:var(--ink)}
.tag{font-family:"Roboto Condensed",sans-serif;font-style:italic;font-weight:700;font-size:8px;line-height:9px;color:var(--ink);text-align:center}
.tag--sludge{left:56px;top:149px}
.tag--ash{left:266px;top:89px}
.tag--mineral{left:180px;top:245px;width:70px}
.note{left:480px;top:22px;width:210px}
.invest__title{left:464px;top:60px;height:24px;width:220px;font-size:17px}
.invest__list{left:482px;top:96px;width:205px}
.invest__list li{margin-bottom:12px}
.product__name{left:500px;width:160px;top:264px;text-align:center;font-family:"Roboto Condensed",sans-serif;font-style:italic;font-weight:700;font-size:15px;line-height:14px;color:var(--ink)}
.product__name small{display:block;font-size:7px;line-height:8px}
.roi{left:480px;width:200px;top:312px;text-align:center;font-family:"Roboto Condensed",sans-serif;font-style:italic;font-weight:700;color:var(--ink);font-size:11px;line-height:14px}
.roi .hl{color:var(--sky-bright);font-size:16px}
.roi .big{color:var(--leaf-dark);font-size:16px}
.carbon__title{left:3px;top:334px;height:22px;width:217px;font-size:12.5px}
.carbon__lead{left:27px;top:368px;font-style:italic;font-size:11px;color:var(--ink)}
.carbon__list{left:72px;top:386px;font-family:"Roboto Condensed",sans-serif;font-style:italic;font-weight:700;font-size:8px;line-height:12.5px;color:var(--forest)}
.usage__title{left:241px;top:296px;height:34px;width:180px;font-size:12px;line-height:13px;border-radius:12px}
.usage__box{left:246px;top:337px;width:211px;height:97px;border-radius:8px;background:rgba(255,255,255,.25);padding:6px 6px 0}
.usage__list{list-style:none;font-family:"Roboto Condensed",sans-serif;font-style:italic;font-weight:700;font-size:8px;line-height:12.4px;color:var(--ink)}
.usage__list li{position:relative;padding-left:12px}
.usage__list li::before{content:"";position:absolute;left:0;top:2.5px;width:7px;height:7px;border-radius:50%;background:#f6e43a}
.usage__list li::after{content:"";position:absolute;left:2px;top:4px;width:3px;height:1.6px;border-left:1.2px solid var(--forest);border-bottom:1.2px solid var(--forest);transform:rotate(-45deg)}
</style>
</head>
<body>

<!-- Outside spread -->
<section class="sheet sheet--outside">
  <div style="left:0;top:0;width:233px;height:250px;background:radial-gradient(circle at 60% 40%,#9a6a4a,#5a3322 70%)" role="img" aria-label="Close-up photo of a young seedling sprouting from dark soil"></div>
  <div style="left:233px;top:30px;width:464px;height:310px;background:radial-gradient(ellipse at 45% 55%,#8fcf3c,#3d7a1a 60%,#254d12)" role="img" aria-label="Aerial photo of a dense green forest canopy"></div>

  <svg class="shapes" viewBox="0 0 697 539" aria-hidden="true">
    <defs>
      <linearGradient id="gFieldTop" x1="0" y1="0" x2="1" y2="1">
        <stop offset="0" stop-color="#8ccb45"/><stop offset="1" stop-color="#4fa82a"/>
      </linearGradient>
      <linearGradient id="gSkyTop" x1="0" y1="0" x2="1" y2="0">
        <stop offset="0" stop-color="#1a6fd8"/><stop offset="1" stop-color="#2aaaf2"/>
      </linearGradient>
    </defs>
    <path d="M233 0H697V95C600 78 450 22 233 42Z" fill="#fff"/>
    <path d="M233 42C450 22 600 78 697 95" fill="none" stroke="#7cc242" stroke-width="3"/>
    <path d="M233 330C380 338 520 300 697 228V539H233Z" fill="url(#gFieldTop)"/>
    <path d="M233 330C380 338 520 300 697 228" fill="none" stroke="#c8ec7a" stroke-width="3" opacity=".8"/>
    <path d="M440 539C530 505 620 482 697 470V484C620 492 545 512 480 539Z" fill="#fff"/>
    <path d="M480 539C545 512 620 492 697 484V539Z" fill="url(#gSkyTop)"/>
    <rect x="233" y="519" width="250" height="20" fill="url(#gSkyTop)"/>
    <path d="M0 215C80 195 170 205 233 232V262C170 238 80 232 0 252Z" fill="url(#gSkyTop)"/>
    <path d="M0 205C80 188 170 198 233 222" fill="none" stroke="#7cc242" stroke-width="3"/>
    <path d="M0 252C80 232 170 238 233 262V539H0Z" fill="#fff"/>
    <rect x="0" y="519" width="233" height="20" fill="#2e5416"/>
  </svg>

  <div role="img" aria-label="Illustration of the earth globe with a green sprout" style="left:593px;top:238px;width:90px;height:90px;border-radius:50%;background:radial-gradient(circle at 35% 35%,#d9f3a5,#5fb52a 70%);box-shadow:0 0 0 3px #fff"></div>

  <div class="brand"><span class="brand__dot"></span>CAELUM PETRA</div>

  <h2 class="pill challenge__title">GLOBAL CHALLENGE:</h2>
  <p class="challenge__lead">Dealing with waste sludge:</p>
  <ul class="bullets challenge__list">
    <li><b>TECHNOLOGY LINE - TL</b> directly answers the burning issue of waste sludge, and with it's patented mineralisation process turns sludge into valuable and safe composite; to be used mainly in construction.</li>
    <li><b>TECHNOLOGY LINE - TL</b> is approved by the Regional Agency for Green Innovation (RAGI);</li>
  </ul>
  <p class="certified">TL is a green technology<br>and is <span class="hl">fully certified</span><br>and recognised by the most<br><span class="hl hl--big">trusted authorities!</span></p>
  <p class="url" style="left:0;top:523px">WWW.CAELUM-PETRIX.COM</p>

  <h3 class="connect__title">LET,S CONNECT</h3>
  <div class="connect__box"></div>
  <div class="contact contact--address">
    <span class="contact__icon"><svg width="11" height="11" viewBox="0 0 12 12"><path d="M1 6L6 1.5 11 6M2.5 5V11H9.5V5" fill="none" stroke="#fff" stroke-width="1.3"/></svg></span>
    <div><p class="contact__label">ADDRESS</p>Stonework d.o.o, Lipova ulica 14<br>2000 Maribor, Slovenia</div>
  </div>
  <div class="contact contact--phone">
    <span class="contact__icon"><svg width="11" height="11" viewBox="0 0 12 12"><path d="M3 1L5 3.5 4 5C5 7 6 8 7.5 8.5L9 7.5 11 9.5 9.5 11C5 10.5 1.5 7 1 2.5Z" fill="none" stroke="#fff" stroke-width="1.1"/></svg></span>
    <div><p class="contact__label">PHONE</p>+123 4567 8900<br>+123 4567 8900</div>
  </div>
  <div class="contact contact--email">
    <span class="contact__icon"><svg width="11" height="11" viewBox="0 0 12 12"><rect x="1" y="3" width="10" height="7" fill="none" stroke="#fff" stroke-width="1.1"/><path d="M1 3L6 7 11 3" fill="none" stroke="#fff" stroke-width="1.1"/></svg></span>
    <div><p class="contact__label">EMAIL</p>caelumpetra@gmail.com<br>hello@caelum-petrix.com</div>
  </div>
  <p class="url" style="left:233px;top:524px">WWW.CAELUM-PETRIX.COM</p>

  <div class="mission">
    <p class="mission__kicker">TECHNICAL SOLUTION FOR MAJOR</p>
    <p class="mission__head">ECOLOGICAL ISSUE</p>
    <p class="mission__line">CAELUM PETRA IS AN INSPIRATIONAL MOVEMENT<br>THAT HAS <span>DECIDED TO PROMOTE</span></p>
    <p class="mission__tag">#NECESSARY CHANGE</p>
  </div>
  <div class="direct">
    <p class="direct__phone">123.456.7890</p>
    <p class="direct__web">www.caelum-petrix.com</p>
  </div>
</section>

<!-- Inside spread -->
<section class="sheet sheet--inside">
  <div role="img" aria-label="3D render of the technology line: loader feeding sludge into hopper, silo, conveyors and a truck receiving composite" style="left:40px;top:10px;width:390px;height:230px;background:linear-gradient(160deg,#f4f4f4,#d9dde0 60%,#b9c0c6);clip-path:polygon(8% 40%,55% 0,100% 30%,95% 95%,10% 100%)"></div>
  <div role="img" aria-label="Line illustration of a money plant growing coins in a pot, with clouds and sun" style="left:475px;top:362px;width:210px;height:76px;background:radial-gradient(ellipse,#e7f5cf,rgba(255,255,255,0) 70%)"></div>

  <svg class="shapes" viewBox="0 0 697 537" aria-hidden="true">
    <defs>
      <linearGradient id="gFieldIn" x1="0" y1="0" x2="1" y2="1">
        <stop offset="0" stop-color="#9ad54e"/><stop offset="1" stop-color="#5fb22c"/>
      </linearGradient>
      <linearGradient id="gSkyIn" x1="0" y1="0" x2="1" y2="0">
        <stop offset="0" stop-color="#1a6fd8"/><stop offset="1" stop-color="#2aaaf2"/>
      </linearGradient>
    </defs>
    <path d="M0 180C60 240 180 268 330 262C400 258 440 252 467 246C300 240 120 262 0 300Z" fill="url(#gSkyIn)"/>
    <path d="M0 196C70 248 190 270 330 268" fill="none" stroke="#fff" stroke-width="4"/>
    <path d="M0 300C120 262 300 240 467 246V470H0Z" fill="url(#gFieldIn)"/>
    <path d="M0 300C120 262 300 240 467 246" fill="none" stroke="#d8f29a" stroke-width="3"/>
    <path d="M0 432C120 440 220 478 330 474C460 470 600 440 697 445V537H0Z" fill="url(#gSkyIn)"/>
    <path d="M0 432C120 440 220 478 330 474C460 470 600 440 697 445" fill="none" stroke="#fff" stroke-width="5"/>
    <!-- flow arrows -->
    <path d="M112 112C140 100 168 106 186 125" fill="none" stroke="#6dbb30" stroke-width="9"/>
    <path d="M180 113L198 134 172 136Z" fill="#6dbb30"/>
    <path d="M265 70C255 100 262 120 278 135" fill="none" stroke="#6dbb30" stroke-width="9"/>
    <path d="M266 138L290 144 288 122Z" fill="#6dbb30"/>
    <path d="M240 200C262 192 276 176 280 158" fill="none" stroke="#6dbb30" stroke-width="9"/>
    <path d="M268 162L282 144 292 166Z" fill="#6dbb30"/>
    <path d="M394 160C430 150 470 158 492 175L500 162 510 205 466 198 480 188C460 175 430 170 398 178Z" fill="#6dbb30"/>
  </svg>

  <div role="img" aria-label="Photo of a waste sludge heap with an excavator" style="left:44px;top:74px;width:72px;height:72px;border-radius:50%;background:radial-gradient(#7a5a3c,#4a3322);box-shadow:0 0 0 3px #6dbb30"></div>
  <div role="img" aria-label="Photo of grey waste ash close-up" style="left:254px;top:13px;width:72px;height:72px;border-radius:50%;background:radial-gradient(#d0d0d0,#555);box-shadow:0 0 0 3px #6dbb30"></div>
  <div role="img" aria-label="Photo of the mineralisation process inside the plant" style="left:180px;top:172px;width:72px;height:72px;border-radius:50%;background:radial-gradient(#b9bec4,#4b5058);box-shadow:0 0 0 3px #6dbb30"></div>

  <p class="tag tag--sludge">WASTE SLUDGE</p>
  <p class="tag tag--ash">WASTE ASH</p>
  <p class="tag tag--mineral">MINERALISATION<br>PROCESS</p>
  <p class="spec">LIFESPAN: 20 YEARS<br>CAPACITY: 21.600T/YEAR.<br>SIZE: 15X20M2<br>WARRANTY: 24 MONTHS</p>

  <ul class="bullets note"><li><b>TL is a GREEN TECHNOLOGY</b> and is fully certified and recognised by the most trusted authorities.</li></ul>
  <h2 class="pill invest__title">SUPERIOR INVESTMENT:</h2>
  <ul class="bullets invest__list">
    <li>Sludge disposal costs increase daily with no other sustainable solution in sight.</li>
    <li>Unique business opportunity with no current competition.</li>
  </ul>
  <div role="img" aria-label="Photo of a cylindrical grey composite block" style="left:526px;top:150px;width:110px;height:110px;border-radius:50%;background:radial-gradient(circle at 40% 40%,#d8d8d8,#8a8a8a 75%)"></div>
  <p class="product__name">END PRODUCT<small>(REUSABLE COMPOSITE SUITABLE<br>FOR CONSTRUCTION)</small></p>
  <p class="roi">Investor can <span class="hl">EXPECT</span><br>a <span class="hl">FULL ROI</span> in under<br><span class="big">2 YEARS.</span></p>

  <h2 class="pill carbon__title">CARBON NEGATIVE TECHNOLOGY</h2>
  <p class="carbon__lead">Technology line can process:</p>
  <ul class="bullets carbon__list">
    <li>MUNICIPAL SLUDGE</li>
    <li>INDUSTRIAL SLUDGE</li>
    <li>WASTE ASH</li>
  </ul>

  <h2 class="pill usage__title">USAGE OF CONSTRUCTION<br>COMPOSITE</h2>
  <div class="usage__box">
    <ul class="usage__list">
      <li>Water impermeable landfill capping.</li>
      <li>Road and service areas on landfills construction.</li>
      <li>Roadbed construction.</li>
      <li>Sewage pipelines bed construction.</li>
      <li>Ant flooding embankments construction.</li>
      <li>Road embankments construction.</li>
      <li>Other construction elements (blocks, bricks).</li>
    </ul>
  </div>

  <p class="url" style="left:0;top:511px">WWW.CAELUM-PETRIX.COM</p>
  <p class="url" style="left:233px;top:511px">WWW.CAELUM-PETRIX.COM</p>
  <p class="url" style="left:464px;top:511px">WWW.CAELUM-PETRIX.COM</p>
</section>

</body>
</html>
```